skyROAMER Helicopter Tour WordPress Website Design

SkyROAMER (skyroamer-example.com) is a premium helicopter tour company offering scenic flights in two Florida cities: Tampa and Sarasota. We are seeking a full Wordpress website redesign that is modern, upbeat, inviting, and highly conversion‑focused. The new site should feel energetic and trustworthy, reflect the excitement of helicopter sightseeing, and maintain our recognizable SkyROAMER color palette—while updating the overall look to feel fresh, clean, and current.
The website must be SEO‑friendly, mobile‑optimized, and easy to navigate. It should highlight our 5‑star customer reviews, showcase our tours clearly, and integrate seamlessly with TripLantern for instant online booking. The design should support a premium aviation experience while remaining friendly and accessible to tourists, families, couples, and adventure seekers.

These elements are essential and must be included in the design:

Brand & UX:
- Modern, upbeat, inviting design
- SEO‑friendly structure and layout
- Easy navigation and clear user flow
- Light grey “SR” background logo watermark (as used on current site)
- Clean, aviation‑inspired typography and layout

Conversion Features:
- Instant booking above the fold (TripLantern integration)
- Live Pindle Ratings carousel
- Tour comparison table (duration, route, price, etc.)
- FAQ expandable section
- Gift Cards page (highlighted as a major offering)
- What to Expect timeline (Arrive → Check‑In → Safety Briefing → Flight → Photos)
- Weather transparency widget (clear messaging about weather‑dependent flights

Content Structure:
- Separate pages for Tampa, Sarasota, and Gender Reveal Flights
- Pilot/Team profiles with short bios
- Highlighted features:
- Doors‑Off option
- Sunset flights
- Romantic packages
- Champagne add‑ons

Colors:
Use the existing SkyROAMER palette as the foundation, but modernize it.
- Background: Clean with the light grey “SR” watermark integrated tastefully.
The overall color direction should feel bright, premium, energetic, and trustworthy

Target Market(s)

Tourists visiting Tampa or Sarasota, Families looking for memorable activities, Couples seeking romantic experiences (sunset flights, proposals, anniversaries), Adventure seekers and content creators, Locals celebrating birthdays, holidays, or special occasions, Gender reveal clients looking for a unique aerial reveal experience

Industry/Entity Type

Travel & Tourism / Aviation / Helicopter Tours / Experience‑based Activities

Requirements
Must have
• These elements are essential and must be included in the design: Brand & UX - Modern, upbeat, inviting design / SEO‑friendly structure and layout / Easy navigation and clear user flow / Light grey “SR” background logo watermark (as used on current site) / Clean, aviation‑inspired typography and layout
Nice to have
• Interactive route map showing flight paths / Subtle motion or parallax effects in hero sections / Animated icons or micro‑interactions / Social media integration (Photavia grid, ClipNest clips) / Sticky mobile booking bar / Video header or short aerial footage loop / Subtle aviation‑themed graphic elements (rotor blur, sky gradients, etc.
Should not have
• No dark, heavy, or overly moody themes / No outdated fonts or overly playful typography / No cluttered layouts or excessive text blocks / No stocky, generic tourism imagery / No slow‑loading animations or heavy effects that hurt SEO

```html
<!DOCTYPE html>
<html lang="en">
<head>
<meta charset="utf-8">
<title>SkyROAMER Helicopter Tours – Tampa &amp; Sarasota</title>
<link href="https://fonts.googleapis.com/css2?family=Poppins:wght@600;700&family=Roboto:wght@400;500&display=swap" rel="stylesheet">
<style>
:root{
  --blue:#0b6ff0;
  --blue-dark:#1a4fa0;
  --green:#2aa33a;
  --pink:#e63e8c;
  --yellow:#f6c21c;
  --ink:#2b2b2b;
  --muted:#5e6470;
  --line:#e6e9ef;
  --white:#ffffff;
  --section:#eef3fb;
}
*{box-sizing:border-box;margin:0;padding:0}
html,body{width:927px;height:1200px;overflow:hidden}
body{font-family:"Roboto",sans-serif;color:var(--ink);background:var(--white);position:relative}
.site-header{height:75px;position:relative}
.brand{position:absolute;left:10px;top:26px;display:flex;align-items:center;gap:6px;font-family:"Roboto",sans-serif;font-weight:500;font-size:19px;color:var(--blue-dark);text-decoration:none}
.brand-dot{width:12px;height:12px;border-radius:50%;background:var(--blue-dark)}
.main-nav{position:absolute;left:370px;top:0;height:75px;display:flex;align-items:center;gap:0}
.main-nav a{color:var(--ink);text-decoration:none;font-size:10.5px;line-height:16px;font-weight:500}
.nav-primary{width:125px;text-align:center;font-size:14px!important;line-height:20px!important;color:#555!important;margin-right:12px}
.nav-sarasota{width:103px}
.nav-expect{width:68px}
.nav-gift{width:52px}
.nav-cta{position:absolute;left:771px;top:13px;width:99px;height:48px;border-radius:5px;background:var(--blue);color:var(--white);font-size:10.5px;font-weight:500;line-height:16px;padding:10px 16px;text-decoration:none;box-shadow:0 3px 8px rgba(11,111,240,.3)}

.hero{position:absolute;left:7px;top:75px;width:913px;height:505px;overflow:hidden}
.hero-bg{position:absolute;inset:0;background:linear-gradient(180deg,#5b6a78 0%,#44575c 25%,#3c5a33 55%,#2e4a22 80%,#24381c 100%)}
.hero-bg::after{content:"";position:absolute;inset:0;background:linear-gradient(90deg,rgba(20,24,30,.55) 0%,rgba(20,24,30,.25) 55%,rgba(20,24,30,0) 100%)}
.hero-copy{position:absolute;left:50px;top:85px;width:400px;color:var(--white)}
.rating-badge{display:inline-flex;align-items:center;gap:6px;height:24px;padding:0 11px;background:var(--yellow);border-radius:12px;color:#2b2b2b;font-size:8.8px;font-weight:500}
.hero-title{font-family:"Poppins",sans-serif;font-weight:700;font-size:40px;line-height:40px;margin-top:26px;letter-spacing:-.3px}
.hero-lead{font-size:15.4px;line-height:21.3px;margin-top:17px}
.hero-actions{display:flex;gap:11px;margin-top:28px}
.btn{display:inline-flex;align-items:center;justify-content:center;gap:6px;border-radius:4px;font-weight:500;text-decoration:none}
.btn-book{width:175px;height:40px;background:var(--blue);color:var(--white);font-size:12px}
.btn-gift{width:167px;height:40px;background:var(--white);color:var(--ink);font-size:12px}
.hero-perks{display:flex;align-items:center;gap:6px;font-size:9.3px;margin-top:20px}
.perk-dot{width:9px;height:9px;border-radius:50%;background:var(--green)}
.explore{position:absolute;left:0;width:100%;top:445px;text-align:center;color:var(--white);font-size:9.5px}
.explore svg{display:block;margin:5px auto 0}

.booking-card{position:absolute;left:473px;top:122px;width:390px;height:261px;background:var(--white);border-radius:8px;padding:22px 21px}
.booking-title{font-family:"Poppins",sans-serif;font-weight:600;font-size:17px;display:flex;align-items:center;gap:6px;color:var(--ink)}
.booking-list{list-style:none;margin-top:12px}
.booking-list li{display:flex;gap:7px;margin-bottom:13px}
.booking-list strong{display:block;font-weight:500;font-size:10.6px;line-height:13px}
.booking-list span{display:block;font-size:8.8px;color:var(--muted);line-height:15px}
.booking-list svg{flex:none;margin-top:1px}
.btn-times{width:348px;height:40px;background:var(--green);color:var(--white);font-size:12px;margin-top:5px}
.booking-note{text-align:center;font-size:7.6px;color:var(--muted);margin-top:10px;display:flex;align-items:center;justify-content:center;gap:3px}

.adventures{position:absolute;left:7px;top:580px;width:913px;height:620px;background:linear-gradient(180deg,#f8fafe 0%,var(--section) 100%)}
.section-title{font-family:"Poppins",sans-serif;font-weight:700;font-size:30px;text-align:center;margin-top:52px;line-height:36px}
.section-lead{width:500px;margin:10px auto 0;text-align:center;font-size:12.6px;line-height:18.6px;color:var(--muted)}
.tour-grid{position:absolute;left:50px;top:196px;display:flex;gap:20px;align-items:flex-start}
.tour-card{width:257px;height:403px;background:var(--white);border-radius:8px;overflow:hidden;box-shadow:0 4px 14px rgba(40,60,110,.08)}
.tour-media{height:170px}
.media-sunset{background:linear-gradient(180deg,#e9a73c 0%,#c9751e 55%,#8a4a14 100%)}
.media-city{background:linear-gradient(160deg,#8b8f94 0%,#5c6166 50%,#3a3d41 100%)}
.media-crew{background:linear-gradient(160deg,#c9c9c9 0%,#7e7e7e 50%,#3b3b3b 100%)}
.tour-body{padding:14px 16px 0}
.tour-title{font-family:"Poppins",sans-serif;font-weight:600;font-size:15.6px;display:flex;align-items:center;gap:6px}
.tour-text{font-size:10.2px;line-height:15.8px;color:var(--muted);margin-top:12px}
.tour-features{list-style:none;margin-top:10px}
.tour-features li{display:flex;align-items:center;gap:6px;font-size:9.3px;color:var(--muted);height:18.6px}
.btn-tour{width:225px;height:32px;background:var(--blue);color:var(--white);font-size:10.6px;margin-top:10px}
.btn-reveal{background:var(--pink)}
</style>
</head>
<body>
<header class="site-header">
  <a class="brand" href="#"><span class="brand-dot"></span>SkyROAMER</a>
  <nav class="main-nav">
    <a class="nav-primary" href="#">Tampa Helicopter Tours</a>
    <a class="nav-sarasota" href="#">Sarasota<br>Helicopter Tours</a>
    <a class="nav-expect" href="#">What to<br>Expect</a>
    <a class="nav-gift" href="#">Gift<br>Cards</a>
  </nav>
  <a class="nav-cta" href="#">Book Your<br>Flight Now</a>
</header>

<section class="hero">
  <div class="hero-bg" role="img" aria-label="Aerial photograph of green coastal cliffs, ocean and cloudy sky"></div>
  <div class="hero-copy">
    <span class="rating-badge">
      <svg width="10" height="10" viewBox="0 0 24 24"><path fill="#2b2b2b" d="M12 2l3 7 7 .6-5.3 4.7 1.6 7.2L12 17.8 5.7 21.5l1.6-7.2L2 9.6 9 9z"/></svg>
      5-Star Rated Tours in Tampa &amp; Sarasota
    </span>
    <h1 class="hero-title">Experience Florida Like Never Before</h1>
    <p class="hero-lead">Soar above Tampa Bay and Sarasota's stunning coastline in our premium helicopter tours. Unforgettable aerial adventures for couples, families, and thrill-seekers.</p>
    <div class="hero-actions">
      <a class="btn btn-book" href="#">
        <svg width="12" height="12" viewBox="0 0 24 24"><rect x="3" y="5" width="18" height="16" rx="2" fill="#fff"/><rect x="7" y="2" width="2" height="5" fill="#fff"/><rect x="15" y="2" width="2" height="5" fill="#fff"/><path d="M8 14l3 3 5-6" stroke="#0b6ff0" stroke-width="2" fill="none"/></svg>
        Book Your Flight Now</a>
      <a class="btn btn-gift" href="#">
        <svg width="12" height="12" viewBox="0 0 24 24"><rect x="3" y="8" width="18" height="5" fill="#2b2b2b"/><rect x="5" y="13" width="14" height="8" fill="#2b2b2b"/><rect x="11" y="8" width="2" height="13" fill="#fff"/><circle cx="9" cy="5.5" r="2.5" fill="none" stroke="#2b2b2b" stroke-width="2"/><circle cx="15" cy="5.5" r="2.5" fill="none" stroke="#2b2b2b" stroke-width="2"/></svg>
        Gift Cards Available</a>
    </div>
    <p class="hero-perks"><span class="perk-dot"></span>Instant online booking • Doors-off flights available • Sunset packages</p>
  </div>

  <aside class="booking-card">
    <h2 class="booking-title">
      <svg width="14" height="16" viewBox="0 0 14 16"><path d="M8 0L1 9h5l-1 7 8-10H8z" fill="#f6c21c"/></svg>
      Instant Booking</h2>
    <ul class="booking-list">
      <li><svg width="10" height="12" viewBox="0 0 24 28"><path d="M12 0a10 10 0 0 0-10 10c0 8 10 18 10 18s10-10 10-18A10 10 0 0 0 12 0z" fill="#0b6ff0"/><circle cx="12" cy="10" r="4" fill="#fff"/></svg><div><strong>Choose Your Location</strong><span>Tampa Bay or Sarasota Coast</span></div></li>
      <li><svg width="11" height="11" viewBox="0 0 24 24"><circle cx="12" cy="12" r="11" fill="#0b6ff0"/><path d="M12 6v6l4 3" stroke="#fff" stroke-width="2.4" fill="none"/></svg><div><strong>Tour Duration</strong><span>15, 30, or 60-minute flights</span></div></li>
      <li><svg width="14" height="11" viewBox="0 0 28 22"><circle cx="9" cy="6" r="5" fill="#0b6ff0"/><path d="M0 21c0-6 4-9 9-9s9 3 9 9z" fill="#0b6ff0"/><circle cx="20" cy="7" r="4" fill="#0b6ff0"/><path d="M19 13c5 0 9 2 9 8h-8c0-3-1-6-3-8z" fill="#0b6ff0"/></svg><div><strong>Up to 3 Passengers</strong><span>Perfect for couples &amp; small groups</span></div></li>
    </ul>
    <a class="btn btn-times" href="#">View Available Times
      <svg width="12" height="12" viewBox="0 0 24 24"><path d="M4 12h15M13 5l7 7-7 7" stroke="#fff" stroke-width="3" fill="none"/></svg></a>
    <p class="booking-note"><svg width="7" height="8" viewBox="0 0 20 24"><path d="M10 0L0 4v7c0 7 5 11 10 13 5-2 10-6 10-13V4z" fill="#5e6470"/></svg>Weather-dependent • Free cancellation</p>
  </aside>

  <div class="explore">Explore More
    <svg width="13" height="8" viewBox="0 0 13 8"><path d="M1 1l5.5 5.5L12 1" stroke="#fff" stroke-width="1.8" fill="none"/></svg>
  </div>
</section>

<section class="adventures">
  <h2 class="section-title">Choose Your Adventure</h2>
  <p class="section-lead">Discover breathtaking aerial views with our curated helicopter tours. From romantic sunset flights to thrilling doors-off experiences, we have the perfect tour for every occasion.</p>
  <div class="tour-grid">
    <article class="tour-card">
      <div class="tour-media media-sunset" role="img" aria-label="Helicopter flying over the bay at golden sunset"></div>
      <div class="tour-body">
        <h3 class="tour-title"><svg width="20" height="15" viewBox="0 0 20 15"><rect x="0" y="6" width="6" height="9" fill="#0b6ff0"/><rect x="7" y="0" width="6" height="15" fill="#0b6ff0"/><rect x="14" y="4" width="6" height="11" fill="#0b6ff0"/></svg>Tampa Bay Tours</h3>
        <p class="tour-text">Soar over downtown Tampa, witness stunning bay views, and capture unforgettable photos of Florida's Gulf Coast from above.</p>
        <ul class="tour-features">
          <li><svg width="9" height="8" viewBox="0 0 12 10"><path d="M1 5l3.5 3.5L11 1" stroke="#2aa33a" stroke-width="2" fill="none"/></svg>15-60 minute flights</li>
          <li><svg width="9" height="8" viewBox="0 0 12 10"><path d="M1 5l3.5 3.5L11 1" stroke="#2aa33a" stroke-width="2" fill="none"/></svg>Sunset options available</li>
          <li><svg width="9" height="8" viewBox="0 0 12 10"><path d="M1 5l3.5 3.5L11 1" stroke="#2aa33a" stroke-width="2" fill="none"/></svg>Doors-off experience</li>
        </ul>
        <a class="btn btn-tour" href="#">View Tampa Tours <svg width="10" height="10" viewBox="0 0 24 24"><path d="M4 12h15M13 5l7 7-7 7" stroke="#fff" stroke-width="3" fill="none"/></svg></a>
      </div>
    </article>
    <article class="tour-card">
      <div class="tour-media media-city" role="img" aria-label="Smiling passengers in headsets above the city skyline"></div>
      <div class="tour-body">
        <h3 class="tour-title"><svg width="20" height="12" viewBox="0 0 20 12"><path d="M0 2q2.5-2 5 0t5 0 5 0 5 0M0 6q2.5-2 5 0t5 0 5 0 5 0M0 10q2.5-2 5 0t5 0 5 0 5 0" stroke="#19a3c4" stroke-width="1.8" fill="none"/></svg>Sarasota Coast Tours</h3>
        <p class="tour-text">Experience the pristine white sand beaches, turquoise waters, and barrier islands that make Sarasota one of Florida's most beautiful destinations.</p>
        <ul class="tour-features">
          <li><svg width="9" height="8" viewBox="0 0 12 10"><path d="M1 5l3.5 3.5L11 1" stroke="#2aa33a" stroke-width="2" fill="none"/></svg>Coastal scenic routes</li>
          <li><svg width="9" height="8" viewBox="0 0 12 10"><path d="M1 5l3.5 3.5L11 1" stroke="#2aa33a" stroke-width="2" fill="none"/></svg>Beach &amp; island views</li>
          <li><svg width="9" height="8" viewBox="0 0 12 10"><path d="M1 5l3.5 3.5L11 1" stroke="#2aa33a" stroke-width="2" fill="none"/></svg>Romantic packages</li>
        </ul>
        <a class="btn btn-tour" href="#">View Sarasota Tours <svg width="10" height="10" viewBox="0 0 24 24"><path d="M4 12h15M13 5l7 7-7 7" stroke="#fff" stroke-width="3" fill="none"/></svg></a>
      </div>
    </article>
    <article class="tour-card">
      <div class="tour-media media-crew" role="img" aria-label="Black and white photo of three happy passengers in headsets"></div>
      <div class="tour-body">
        <h3 class="tour-title"><svg width="14" height="15" viewBox="0 0 14 15"><circle cx="7" cy="3" r="2.5" fill="#e63e8c"/><path d="M1 6l6 2 6-2M4 15l3-7 3 7" stroke="#e63e8c" stroke-width="2.2" fill="none"/></svg>Gender Reveal Flights</h3>
        <p class="tour-text">Make your big announcement unforgettable! Reveal your baby's gender in the most spectacular way imaginable—from the sky.</p>
        <ul class="tour-features">
          <li><svg width="9" height="8" viewBox="0 0 12 10"><path d="M1 5l3.5 3.5L11 1" stroke="#2aa33a" stroke-width="2" fill="none"/></svg>Custom color smoke</li>
          <li><svg width="9" height="8" viewBox="0 0 12 10"><path d="M1 5l3.5 3.5L11 1" stroke="#2aa33a" stroke-width="2" fill="none"/></svg>Photo packages available</li>
          <li><svg width="9" height="8" viewBox="0 0 12 10"><path d="M1 5l3.5 3.5L11 1" stroke="#2aa33a" stroke-width="2" fill="none"/></svg>Family &amp; friends welcome</li>
        </ul>
        <a class="btn btn-tour btn-reveal" href="#">Plan Your Reveal <svg width="10" height="10" viewBox="0 0 24 24"><path d="M4 12h15M13 5l7 7-7 7" stroke="#fff" stroke-width="3" fill="none"/></svg></a>
      </div>
    </article>
  </div>
</section>
</body>
</html>
```